依頼詳細
トップページのデザイン トップページとサブページ(2ページ目以降)のデザイン サブページは、トップページのデザインを引き継ぐ感じで
グローバルナビ  ワードプレス×レスポンシブで制作予定

全体的なイメージ https://www.morino-kobo.jp/index.html
青とホワイトを基調にした清潔感があり ごちゃごちゃしすぎず
患者さんの視線で見やすく 探しやすい感じを希望します。
お子様や女性にも好まれるような可愛いイラストなどもお願いします。

グローバルナビに入れる予定の項目 Q&A、アクセス、医院紹介、治療内容、マウスピース矯正、費用、部分矯正、裏側矯正

トップページに記載したい文章
マウスピース型矯正装置(クリアフィット)をメインの紹介するサイト
裏側矯正にも力入れており、見えないMIX (マウスピース矯正と裏側矯正の組み合わせで幅広く対応できる。

最新式 デジタルスキャナー dento scope の紹介
参考https://hanawa-dent.jp/orthodontic/clearfit/

ブログ形式で 新着情報
休診日・診療時間/
ご相談・お問い合わせ

希望イメージ
シンプル 複雑
単色 カラフル
暗い 明るい
日常 高級
遊び心 厳粛
未来的 伝統的
女性的 男性的
希望する色
水色系
納品ファイル
• 高解像度JPG (.jpg)
• フォトショップ形式 (.psd)
補足説明
マウスピース矯正を マウスピース型矯正装置
クリアフィット をマウスピース型矯正装置(クリアフィット)

※医療広告の関係で表記を統一してください。
用語は、マウスピース型矯正装置(クリアフィット)を徹底してください。

高校生~20代女性に響くような デザインが希望です。

透明で見ないこと 取り外せること
最新式 3Dスキャンナー dento scoopeを導入していること
dento scope により、簡易シュミレーションが見れること
裏側矯正も得意なことから 組み合わせることによって対応できる
幅が広がったこと。

を強調したデザインが希望です。

参照https://www.kirari-ha.jp/simulation/

なるべく裏側矯正の内容は、記載しないでマウスピース型矯正装置(クリアフィット)の内容だけにしたい。

よろしくお願いします。

```html
<!DOCTYPE html>
<html lang="ja">
<head>
<meta charset="utf-8">
<title>みなと橋 ことり矯正歯科 | マウスピース型矯正装置（クリアフィット）</title>
<link rel="stylesheet" href="https://fonts.googleapis.com/css2?family=Noto+Sans+JP:wght@300;400;500;700&family=Noto+Serif+JP:wght@400;500;600&family=Cormorant+Garamond:wght@400;500;600&display=swap">
<style>
:root{
  --blue:#5ba4d4;
  --blue-deep:#3d86bb;
  --blue-soft:#a9d2ec;
  --pale:#eef6fb;
  --pale-2:#f6fafd;
  --ink:#4a5560;
  --ink-light:#8a96a0;
  --line:#d7e8f4;
  --white:#ffffff;
}
*{margin:0;padding:0;box-sizing:border-box}
html,body{width:1200px;height:3948px;overflow:hidden}
body{font-family:"Noto Sans JP",sans-serif;color:var(--ink);background:var(--white);font-size:13px;line-height:1.9}
.en{font-family:"Cormorant Garamond",serif;letter-spacing:.18em}
section,header,footer{position:relative;width:1200px;overflow:hidden}

/* header */
.site-header{height:56px;display:flex;align-items:center;justify-content:space-between;padding:0 40px;background:var(--white)}
.brand{display:flex;align-items:center;gap:8px;font-size:14px;font-weight:500;color:var(--ink);letter-spacing:.08em}
.brand-dot{width:10px;height:10px;border-radius:50%;background:var(--blue)}
.gnav{display:flex;gap:26px;font-size:12px;color:var(--ink);letter-spacing:.06em}

/* hero */
.hero{height:584px;background:linear-gradient(180deg,#f3f9fd 0%,#e6f2fa 100%);text-align:center}
.hero-mark{margin:36px auto 0;width:150px;height:90px;display:flex;flex-direction:column;align-items:center;justify-content:center;gap:4px}
.hero-mark .circle{width:46px;height:46px;border-radius:50%;border:1px solid var(--blue-soft)}
.hero-mark .name{font-size:12px;color:var(--blue-deep);letter-spacing:.2em}
.hero-en{margin-top:22px;font-size:22px;color:var(--blue-deep)}
.hero-title{font-family:"Noto Serif JP",serif;font-size:30px;font-weight:500;color:var(--blue-deep);letter-spacing:.14em;margin-top:2px}
.hero-sub{font-size:12px;color:var(--ink-light);letter-spacing:.14em;margin-top:4px}
.hero-photo{position:absolute;left:0;right:0;bottom:0;height:224px;background:linear-gradient(180deg,#e6f2fa 0%,#d3e7f4 55%,#c3dcec 100%)}

/* section headings */
.sec-head{text-align:center}
.sec-head .en{display:block;font-size:14px;color:var(--blue)}
.sec-head h2{font-family:"Noto Serif JP",serif;font-weight:500;font-size:24px;color:var(--blue-deep);letter-spacing:.12em}
.sec-head .ja-sub{display:block;font-size:12px;color:var(--ink-light);letter-spacing:.14em}
.sec-head .rule{display:block;width:40px;height:1px;background:var(--blue-soft);margin:12px auto 0}

/* about */
.about{height:590px;background:var(--white)}
.about .sec-head{padding-top:70px}
.about-card{position:absolute;left:140px;top:200px;width:920px;height:300px;background:var(--pale-2);display:flex;align-items:center}
.about-photo{width:430px;height:300px;background:linear-gradient(135deg,#f4f9fc 0%,#dcebf5 60%,#c9dfee 100%)}
.about-text{flex:1;padding:0 44px}
.about-text h3{font-family:"Noto Serif JP",serif;font-size:17px;font-weight:500;color:var(--blue-deep);letter-spacing:.1em;margin-bottom:14px}
.about-text p{font-size:11.5px;color:var(--ink);margin-bottom:10px}

/* merit */
.merit{height:450px;background:linear-gradient(180deg,var(--white) 0%,var(--pale) 100%)}
.merit .sec-head{padding-top:50px}
.merit-list{position:absolute;left:100px;top:140px;width:1000px;display:flex;gap:20px;list-style:none}
.merit-item{flex:1;background:var(--white);border:1px solid var(--line);height:186px;padding:14px 10px;text-align:center}
.merit-item .label{font-size:10px;color:var(--blue);letter-spacing:.2em;font-family:"Cormorant Garamond",serif;line-height:1.6}
.merit-item .num{font-family:"Cormorant Garamond",serif;font-size:30px;color:var(--blue-deep);line-height:1.1}
.merit-item svg{display:block;margin:6px auto}
.merit-item h3{font-size:13px;font-weight:500;color:var(--blue-deep);letter-spacing:.06em;line-height:1.7}
.merit-item p{font-size:10px;color:var(--ink-light);line-height:1.6;margin-top:2px}
.btn{display:block;width:200px;height:40px;line-height:38px;border:1px solid var(--blue);background:var(--white);color:var(--blue-deep);font-size:12px;letter-spacing:.14em;text-align:center;position:absolute;left:500px}
.btn::after{content:"";position:absolute;right:16px;top:18px;width:14px;height:1px;background:var(--blue)}
.merit .btn{top:366px}

/* scanner */
.scanner{height:780px;background:var(--pale)}
.scanner .sec-head{padding-top:56px}
.scanner .sec-head h2{font-size:20px;line-height:1.7}
.device{position:absolute;left:120px;top:170px;width:320px;height:330px;background:radial-gradient(circle at 50% 45%,#ffffff 0%,#e3eef6 60%,#d5e6f1 100%)}
.scanner-intro{position:absolute;left:490px;top:190px;width:590px}
.product-name{display:flex;align-items:center;gap:8px;font-size:22px;font-weight:500;color:var(--blue-deep);letter-spacing:.04em}
.product-name .sq{width:16px;height:16px;background:var(--blue)}
.scanner-intro h3{font-family:"Noto Serif JP",serif;font-size:16px;font-weight:500;color:var(--blue-deep);margin:26px 0 10px;letter-spacing:.08em}
.scanner-intro p{font-size:11.5px}
.point-box{position:absolute;left:120px;top:520px;width:960px;background:var(--white);padding:18px 40px 12px}
.point{margin-bottom:8px}
.point h4{font-size:12.5px;font-weight:500;color:var(--blue-deep);display:flex;align-items:center;gap:10px;line-height:1.7}
.point h4::before{content:"";width:22px;height:1px;background:var(--blue)}
.point p{font-size:10.5px;color:var(--ink);padding-left:32px;line-height:1.7}
.scanner .btn{top:722px}

/* blog */
.blog{height:650px;background:var(--white)}
.blog .sec-head{padding-top:60px}
.blog .sec-head .en{font-size:28px;color:var(--blue-deep);letter-spacing:.12em}
.blog-list{position:absolute;left:100px;top:200px;width:1000px;display:flex;gap:24px;list-style:none}
.blog-item{flex:1}
.blog-thumb{height:168px}
.t1{background:linear-gradient(135deg,#f3f6f8,#dfe8ee)}
.t2{background:linear-gradient(135deg,#f7f4f1,#e6e2dc)}
.t3{background:linear-gradient(135deg,#f5f8fa,#e2ebf1)}
.t4{background:linear-gradient(135deg,#f6f9fb,#dcecf6)}
.blog-item time{display:block;font-size:10px;color:var(--blue);margin-top:10px;letter-spacing:.1em}
.blog-item p{font-size:11.5px;line-height:1.7}
.blog .btn{top:560px}

/* access */
.access{height:740px;background:linear-gradient(180deg,var(--white) 0%,var(--pale) 100%)}
.access .sec-head{padding-top:40px}
.access .sec-head .en{font-size:28px;color:var(--blue-deep);letter-spacing:.12em}
.map{position:absolute;left:60px;top:170px;width:560px;height:540px;background:linear-gradient(135deg,#eef1f3 0%,#e1e5e8 100%)}
.access-info{position:absolute;left:668px;top:170px;width:440px}
.access-info h3{font-size:15px;font-weight:500;color:var(--ink);letter-spacing:.08em;padding-bottom:10px;border-bottom:1px solid var(--line)}
.info-block{margin-top:16px}
.info-block h4{font-size:12px;font-weight:500;color:var(--blue-deep);display:flex;align-items:center;gap:10px}
.info-block h4::before{content:"";width:22px;height:1px;background:var(--blue)}
.info-block p{font-size:11.5px;padding-left:32px}
.tel{font-family:"Cormorant Garamond",serif;font-size:26px;color:var(--blue-deep);letter-spacing:.08em;margin-top:16px;display:flex;align-items:center;gap:8px}
.tel-btn{margin-top:10px;width:300px;height:40px;border-radius:20px;background:var(--blue);color:var(--white);font-size:12px;letter-spacing:.12em;display:flex;align-items:center;justify-content:center}
.hours{margin:8px 0 0 32px;border-collapse:collapse;font-size:11px;width:380px}
.hours th,.hours td{border-bottom:1px solid var(--line);padding:4px 4px;text-align:center;font-weight:400}
.hours th:first-child,.hours td:first-child{text-align:left}
.hours-note{margin-top:6px}

/* footer */
.site-footer{height:98px;background:var(--pale);border-top:1px solid var(--line);padding:26px 40px 0}
.footer-row{display:flex;justify-content:space-between;align-items:center}
.copyright{text-align:center;font-size:10px;color:var(--ink-light);margin-top:22px;letter-spacing:.1em}
</style>
</head>
<body>

<header class="site-header">
  <div class="brand"><span class="brand-dot"></span>みなと橋 ことり矯正歯科</div>
  <nav class="gnav"><span>Q&amp;A</span><span>アクセス</span><span>医院紹介</span><span>治療内容</span><span>マウスピース矯正</span><span>費用</span><span>部分矯正</span><span>裏側矯正</span></nav>
</header>

<section class="hero">
  <div class="hero-mark"><span class="circle"></span><span class="name">ことり矯正歯科</span></div>
  <div class="hero-en en">CLEARFIT</div>
  <h1 class="hero-title">マウスピース型矯正装置</h1>
  <p class="hero-sub">目立たず生活を楽しめる、透明な歯科矯正</p>
  <div class="hero-photo" role="img" aria-label="頬に手を添えて微笑む家族や若い女性たちの写真"></div>
</section>

<section class="about">
  <div class="sec-head">
    <h2>マウスピース型矯正装置</h2>
    <span class="ja-sub">（クリアフィット）</span>
    <span class="rule"></span>
  </div>
  <div class="about-card">
    <div class="about-photo" role="img" aria-label="透明なマウスピース型矯正装置の写真"></div>
    <div class="about-text">
      <h3>透明で見えないマウスピース</h3>
      <p>マウスピース型矯正装置（クリアフィット）は、透明な素材で作られた取り外しのできる矯正装置です。装着していても周りの人に気づかれにくく、普段どおりの笑顔で過ごせます。</p>
      <p>食事や歯みがきの時には外せるので、お口の中を清潔に保ちやすいのも特長です。段階ごとに新しいマウスピースへ交換しながら、少しずつ歯を動かしていきます。</p>
    </div>
  </div>
</section>

<section class="merit">
  <div class="sec-head">
    <h2>メリット・特徴</h2>
    <span class="rule"></span>
  </div>
  <ul class="merit-list">
    <li class="merit-item"><div class="label">MERIT</div><div class="num">01</div>
      <svg width="28" height="22" viewBox="0 0 28 22"><path d="M2 11 Q14 -2 26 11 Q14 24 2 11Z" fill="none" stroke="#5ba4d4" stroke-width="1.4"/><circle cx="14" cy="11" r="3.5" fill="none" stroke="#5ba4d4" stroke-width="1.4"/></svg>
      <h3>外見に目立たない</h3><p>透明な装置なので<br>気づかれにくい</p></li>
    <li class="merit-item"><div class="label">MERIT</div><div class="num">02</div>
      <svg width="28" height="22" viewBox="0 0 28 22"><path d="M8 2v18M5 2v6q3 3 6 0V2M20 2q-4 4 0 10v8" fill="none" stroke="#5ba4d4" stroke-width="1.4"/></svg>
      <h3>外して食事ができる</h3><p>食事や歯みがきの時は<br>取り外しできます</p></li>
    <li class="merit-item"><div class="label">MERIT</div><div class="num">03</div>
      <svg width="28" height="22" viewBox="0 0 28 22"><path d="M7 3q7-3 14 0q3 5-1 11l-2 6-3-6h-2l-3 6-2-6q-4-6-1-11Z" fill="none" stroke="#5ba4d4" stroke-width="1.4"/></svg>
      <h3>むし歯リスクが減る</h3><p>清潔に保ちやすく<br>お口の健康を守ります</p></li>
    <li class="merit-item"><div class="label">MERIT</div><div class="num">04</div>
      <svg width="28" height="22" viewBox="0 0 28 22"><circle cx="14" cy="11" r="8" fill="none" stroke="#5ba4d4" stroke-width="1.4"/><path d="M10 11l3 3 5-6" fill="none" stroke="#5ba4d4" stroke-width="1.4"/></svg>
      <h3>金属アレルギーでも</h3><p>金属を使わないため<br>安心して使えます</p></li>
    <li class="merit-item"><div class="label">MERIT</div><div class="num">05</div>
      <svg width="28" height="22" viewBox="0 0 28 22"><path d="M14 19S4 13 4 7a5 5 0 0 1 10-1 5 5 0 0 1 10 1c0 6-10 12-10 12Z" fill="none" stroke="#5ba4d4" stroke-width="1.4"/></svg>
      <h3>痛みが少ない</h3><p>ワイヤーに比べて<br>負担がやわらか</p></li>
  </ul>
  <a class="btn">詳しく見る</a>
</section>

<section class="scanner">
  <div class="sec-head">
    <h2>最新式デジタルスキャナー「dento scope」を導入<br>より快適・正確な治療を</h2>
  </div>
  <div class="device" role="img" aria-label="口腔内3Dスキャナー本体とモニターの写真"></div>
  <div class="scanner-intro">
    <div class="product-name"><span class="sq"></span>dento scope</div>
    <h3>世界で最新鋭の3Dスキャン装置</h3>
    <p>dento scope は、お口の中をスキャンするだけで歯並びを立体データとして取り込める最新のデジタル機器です。型取りの不快感がなく、その場で治療後の歯並びの簡易シミュレーションをご覧いただけます。</p>
  </div>
  <div class="point-box">
    <div class="point"><h4>精度データの取得</h4><p>従来の型取りに比べてより精密なデータを得られるため、装置の適合がよく、仕上がりの精度が高まります。</p></div>
    <div class="point"><h4>スピーディな治療</h4><p>データをすぐに送信できるので、装置の作製までの期間が短くなり、治療をスムーズに始められます。</p></div>
    <div class="point"><h4>快適</h4><p>粘土のような材料を使わないため、嘔吐反射が気になる方やお子さまでも負担なく受けていただけます。</p></div>
  </div>
  <a class="btn">詳しく見る</a>
</section>

<section class="blog">
  <div class="sec-head">
    <span class="en">Blog</span>
    <span class="ja-sub">当院のブログ</span>
  </div>
  <ul class="blog-list">
    <li class="blog-item"><div class="blog-thumb t1" role="img" aria-label="歯科医師と患者のカウンセリング風景の写真"></div><time>2024.04.12</time><p>矯正治療を始める前に知っておきたい大切なポイントのお話</p></li>
    <li class="blog-item"><div class="blog-thumb t2" role="img" aria-label="デスクで作業する女性の写真"></div><time>2024.04.05</time><p>マウスピース型矯正装置と毎日の過ごし方についてのご案内</p></li>
    <li class="blog-item"><div class="blog-thumb t3" role="img" aria-label="歯の模型の写真"></div><time>2024.03.28</time><p>歯並びとむし歯予防の関係をわかりやすくご紹介します</p></li>
    <li class="blog-item"><div class="blog-thumb t4" role="img" aria-label="歯みがきをする子どもの写真"></div><time>2024.03.20</time><p>お子さまの歯並びが気になったら早めにご相談ください</p></li>
  </ul>
  <a class="btn">詳しく見る</a>
</section>

<section class="access">
  <div class="sec-head">
    <span class="en">Access</span>
    <span class="ja-sub">当院へのアクセス</span>
  </div>
  <div class="map" role="img" aria-label="医院周辺の地図"></div>
  <div class="access-info">
    <h3>みなと橋 ことり矯正歯科</h3>
    <div class="info-block"><h4>アクセス</h4><p>東京都中央区みなと橋2-14-6 ことりビル3F<br>みなと橋駅 A2出口より徒歩3分</p></div>
    <div class="tel"><svg width="20" height="20" viewBox="0 0 24 24"><path d="M6.6 10.8a15 15 0 0 0 6.6 6.6l2.2-2.2a1 1 0 0 1 1-.25 11.4 11.4 0 0 0 3.6.57 1 1 0 0 1 1 1V20a1 1 0 0 1-1 1A17 17 0 0 1 3 4a1 1 0 0 1 1-1h3.5a1 1 0 0 1 1 1c0 1.25.2 2.45.57 3.57a1 1 0 0 1-.25 1Z" fill="#3d86bb"/></svg>TEL 03-5550-2187</div>
    <div class="tel-btn">ご予約・ご相談はお電話で</div>
    <div class="info-block"><h4>診療時間</h4>
      <table class="hours">
        <tr><th></th><th>月</th><th>火</th><th>水</th><th>木</th><th>金</th><th>土</th><th>日</th></tr>
        <tr><td>10:00〜13:00</td><td>●</td><td>●</td><td>●</td><td>／</td><td>●</td><td>●</td><td>／</td></tr>
        <tr><td>14:30〜19:00</td><td>●</td><td>●</td><td>●</td><td>／</td><td>●</td><td>▲</td><td>／</td></tr>
      </table>
      <p class="hours-note">▲土曜午後は14:00〜17:00</p>
    </div>
    <div class="info-block"><h4>休診日</h4><p>木曜日・日曜日・祝日</p></div>
  </div>
</section>

<footer class="site-footer">
  <div class="footer-row">
    <div class="brand"><span class="brand-dot"></span>みなと橋 ことり矯正歯科</div>
    <nav class="gnav"><span>Q&amp;A</span><span>アクセス</span><span>医院紹介</span><span>治療内容</span><span>マウスピース矯正</span><span>費用</span><span>部分矯正</span><span>裏側矯正</span></nav>
  </div>
  <p class="copyright">© Minatobashi Kotori Orthodontic Clinic. All Rights Reserved.</p>
</footer>

</body>
</html>
```